Dalton & Vesh Periodontics and Implant Solutions Business Card

We are a specialty dental practice- implants and periodontal surgery. We have just re-designed our logo and are building a new office and would like to re-design our business card. We are looking for something professional with a creative and artsy twist- something to stand out among the rest! Happy Designing!

I have uploaded all versions of our new logo and our current business card. We have 3 locations and 2 doctors.
Updates

Target Market(s)

55+

Industry/Entity Type

Dental

Contact Information for Business Card

Needs Names, logo, locations- professional and artsy!

Colors
0555a3
0592cd
34a7d7
3277b5
85cae6
85acd3
cee9f5
ecf7fb

Requirements
Must have
• our names:
• Gavin T. Dalton D.M.D.
• Marla P. Vesh D.M.D.
• Diplomate of the National Council of Gum Surgery
• Address locations:
• 462 N. Larkspur Avenue Suite 210B Plantation, FL 33324
• Tel: 954-603-2281 Fax: 954-603-2895
• 5174 Hollins Lane #C-3 Boca Raton, FL 33434
• Tel: 561-327-6018 Fax: 561-327-6092
• 381 Northwest 7th Street #412 Miami FL 33131
• Tel: 786-540-3316 Fax: 786-540-3389
Nice to have
• unique look
Should not have
• doesn't need QR like our current card has.

```html
<!DOCTYPE html>
<html lang="en">
<head>
<meta charset="utf-8">
<title>Dalton &amp; Vesh Periodontics and Implant Solutions – Business Card</title>
<link href="https://fonts.googleapis.com/css2?family=Questrial&family=Arimo:wght@400;700&display=swap" rel="stylesheet">
<style>
  :root {
    --navy: #2b3a86;
    --navy-deep: #1f2c6e;
    --blue-bright: #0592cd;
    --blue-sky: #34a7d7;
    --blue-pale: #85cae6;
    --cream: #f3f1e6;
    --ink: #27307a;
    --white: #ffffff;
    --stage: #e6e8ee;
    --divider-light: #c9c9c0;
    --divider-dark: #5563a6;
  }
  * { box-sizing: border-box; margin: 0; padding: 0; }
  html, body { width: 1200px; height: 786px; overflow: hidden; }
  body {
    background: var(--stage);
    display: flex;
    align-items: center;
    justify-content: center;
    gap: 48px;
    font-family: "Questrial", sans-serif;
  }
  .card {
    position: relative;
    width: 540px;
    height: 308px;
    border-radius: 16px;
    overflow: hidden;
    box-shadow: 0 10px 30px rgba(20, 30, 80, 0.18);
  }

  /* Front */
  .card-front { background: var(--cream); color: var(--ink); }
  .front-swoosh { position: absolute; left: 0; bottom: 0; width: 540px; height: 308px; }
  .brand {
    position: absolute;
    display: flex;
    align-items: center;
    gap: 12px;
  }
  .brand-dot {
    flex: none;
    width: 46px; height: 46px;
    border-radius: 50%;
    border: 3px solid currentColor;
    opacity: 0.9;
  }
  .brand-name {
    font-family: "Questrial", sans-serif;
    font-size: 18px;
    line-height: 1.2;
    letter-spacing: 0.3px;
  }
  .card-front .brand { left: 30px; top: 44px; width: 250px; color: var(--ink); }
  .front-divider {
    position: absolute;
    left: 288px; top: 110px;
    width: 1px; height: 150px;
    background: var(--divider-light);
  }
  .doctors {
    position: absolute;
    left: 308px; top: 104px;
    color: var(--ink);
  }
  .doctor-name {
    font-family: "Arimo", sans-serif;
    font-weight: 700;
    font-size: 17px;
  }
  .doctor-name .degree { font-weight: 400; font-family: "Questrial", sans-serif; }
  .doctor-credential {
    font-size: 14px;
    line-height: 1.3;
    margin: 14px 0 16px;
  }

  /* Back */
  .card-back { background: var(--navy); color: var(--white); }
  .card-back .brand { left: 34px; top: 36px; width: 330px; color: var(--white); }
  .card-back .brand-name { font-size: 20px; }
  .locations {
    position: absolute;
    left: 26px; right: 22px; bottom: 34px;
    display: flex;
  }
  .location {
    flex: 1;
    padding: 0 12px;
    font-family: "Arimo", sans-serif;
    font-size: 11.5px;
    line-height: 1.45;
  }
  .location + .location { border-left: 1px solid var(--divider-dark); }
  .location .label { color: var(--blue-sky); font-weight: 700; }
</style>
</head>
<body>

  <section class="card card-front" aria-label="Business card front">
    <svg class="front-swoosh" viewBox="0 0 540 308" aria-hidden="true">
      <path d="M0 178 C 90 250, 230 290, 330 308 L0 308 Z" fill="var(--navy)"/>
      <path d="M0 168 C 95 245, 235 285, 340 308" fill="none" stroke="var(--blue-bright)" stroke-width="7"/>
      <path d="M0 186 C 90 255, 220 292, 318 308" fill="none" stroke="var(--blue-pale)" stroke-width="2"/>
    </svg>

    <div class="brand">
      <span class="brand-dot"></span>
      <p class="brand-name">Dalton &amp; Vesh Periodontics and Implant Solutions</p>
    </div>

    <div class="front-divider"></div>

    <div class="doctors">
      <p class="doctor-name">Gavin T. Dalton <span class="degree">D.M.D.</span></p>
      <p class="doctor-credential">Diplomate of the<br>National Council of<br>Gum Surgery</p>
      <p class="doctor-name">Marla P. Vesh <span class="degree">D.M.D.</span></p>
    </div>
  </section>

  <section class="card card-back" aria-label="Business card back">
    <div class="brand">
      <span class="brand-dot"></span>
      <p class="brand-name">Dalton &amp; Vesh Periodontics and Implant Solutions</p>
    </div>

    <div class="locations">
      <div class="location">
        <p>462 N. Larkspur Avenue<br>Suite 210B Plantation, FL 33324</p>
        <p><span class="label">Tel:</span> 954-603-2281</p>
        <p><span class="label">Fax:</span> 954-603-2895</p>
      </div>
      <div class="location">
        <p>5174 Hollins Lane #C-3<br>Boca Raton, FL 33434</p>
        <p><span class="label">Tel:</span> 561-327-6018</p>
        <p><span class="label">Fax:</span> 561-327-6092</p>
      </div>
      <div class="location">
        <p>381 Northwest 7th Street<br>#412 Miami FL 33131</p>
        <p><span class="label">Tel:</span> 786-540-3316</p>
        <p><span class="label">Fax:</span> 786-540-3389</p>
      </div>
    </div>
  </section>

</body>
</html>
```